Safety Consultancy focusing on developing exceptional Safety Leaders

I need a full but simple, modern, catchy website to drive business - my focus is on helping organizations to understand the impact that leaders have on safety performance and how they build the processes to make that happen. I already have great branding (logos) built through ArtisanHive and can provide all narrative to build out the pages

Target Market(s)

Focused internationally. Typical client has a fairly robust and mature safety culture yet lacks the focused effort to develop all levels of leadership in terms of managing safety. Exercising these competencies results in continued development of an organizations safety culture as well as improved safety performance

Industry/Entity Type

all

Coding

Coded - Design and coding required

Number of Pages Required

4 page

Font styles to use
Other font styles liked:
• to match my branding

Colors
0054AA
0677BA
7BADD7
CADEEF
E8F1F8

Requirements
Must have
• Must utilize my current branding, logo, etc. I want to have a page outlining clearly my vision - which I will add to my uploads as we move forward. I need to have a page listing my extensive and unique experience as well as successes
Nice to have
• Want to leave it up to designers - but needs to be simple and easily navigable - hope to have a resource page that I can update myself with safety resource info, reports, etc.

```html
<!DOCTYPE html>
<html lang="en">
<head>
<meta charset="utf-8">
<title>Halvorn Ventures International — Safety Leadership</title>
<link rel="stylesheet" href="https://fonts.googleapis.com/css2?family=Poppins:wght@400;500;600;700&display=swap">
<style>
:root{
  --navy:#34398a;
  --blue:#0054AA;
  --blue-mid:#0677BA;
  --blue-soft:#7BADD7;
  --blue-pale:#CADEEF;
  --blue-mist:#E8F1F8;
  --ink:#1c1c1c;
  --muted:#555;
  --footer:#2c3441;
  --white:#fff;
}
*{box-sizing:border-box;margin:0;padding:0}
html,body{width:1200px;height:4236px;overflow:hidden}
body{font-family:"Poppins",sans-serif;color:var(--ink);background:var(--white);position:relative}
.abs{position:absolute}
a{color:inherit;text-decoration:none}
.h-section{font-weight:700;color:var(--blue-mid);font-size:34px;text-align:center;letter-spacing:.3px}

/* nav */
.topbar{left:0;top:0;width:1200px;height:57px;background:var(--navy);color:var(--white)}
.brand{display:flex;align-items:center;gap:10px}
.brand-mark{width:30px;height:30px;border-radius:50%;background:var(--white)}
.brand-name{font-weight:600;font-size:24px;line-height:1}
.brand-sub{font-size:9px;line-height:1.2}
.topbar .brand{left:69px;top:12px;position:absolute}
.nav-link{position:absolute;top:19px;font-size:13px}
.nav-link.active{font-weight:600}
.nav-link.active::after{content:"";position:absolute;left:-6px;right:-6px;top:30px;height:2px;background:var(--white)}
.consult{left:942px;top:8px;display:flex;align-items:center;gap:10px}
.consult-icon{width:42px;height:40px;border-radius:6px;background:var(--blue-pale);display:flex;align-items:center;justify-content:center}
.consult small{display:block;font-size:12px}
.consult b{display:block;font-size:13px;font-weight:700}

/* hero */
.hero{left:0;top:57px;width:1200px;height:517px;background:var(--blue-pale);overflow:hidden}
.hero-disc{left:537px;top:-130px;width:770px;height:770px;border-radius:50%;background:var(--blue-mist)}
.hero-portrait{left:682px;top:9px;width:370px;height:508px;border-radius:180px 180px 0 0;background:linear-gradient(180deg,#d9c7bb 0%,#5476b5 40%,#2f4f93 100%)}
.hero h1{left:86px;top:142px;font-size:35px;font-weight:600;line-height:1.3;width:640px}
.hero p{left:86px;top:240px;font-size:17px;line-height:1.6;width:520px}
.signature{left:440px;top:310px;width:175px;height:55px;background:linear-gradient(90deg,rgba(52,57,138,.12),rgba(52,57,138,.2));border-radius:4px}
.btn-primary{background:var(--blue);color:var(--white);font-weight:500;border-radius:5px;display:flex;align-items:center;justify-content:center}
.hero .btn-primary{left:90px;top:380px;width:181px;height:55px;font-size:16px}

/* pillars */
.possible-title{left:0;top:594px;width:1200px}
.possible-lead{left:260px;top:640px;width:680px;text-align:center;font-size:18px;line-height:1.55}
.pillar{top:730px;width:320px;text-align:center}
.pillar-ring{margin:0 auto;width:190px;height:190px;border-radius:50%;border:2px dashed var(--blue-soft);display:flex;align-items:center;justify-content:center}
.pillar-ring span{width:172px;height:172px;border-radius:50%;background:var(--blue-mist);display:flex;align-items:center;justify-content:center}
.pillar h3{margin-top:22px;font-size:18px;font-weight:500}
.pillar p{margin:14px auto 0;width:250px;font-size:13px;line-height:1.4}

/* vision */
.vision{left:82px;top:1087px;width:1034px;height:449px;border-radius:6px;overflow:hidden}
.vision-photo{left:0;top:0;width:1034px;height:449px;background:linear-gradient(120deg,#caa35a 0%,#6d6a62 30%,#3d4048 60%,#1c1f26 100%)}
.vision-menu{left:36px;top:33px;width:226px;height:381px;background:var(--white);border-radius:4px;overflow:hidden;box-shadow:0 6px 18px rgba(0,0,0,.15)}
.vision-menu .xp{height:85px;background:var(--blue-mist);display:flex;align-items:center;gap:12px;padding-left:24px}
.vision-menu .xp b{font-size:38px;font-weight:400;color:var(--blue)}
.vision-menu .xp span{font-size:12px;line-height:1.3}
.vision-menu li{list-style:none;height:59px;display:flex;align-items:center;justify-content:space-between;padding:0 14px 0 24px;font-size:18px;font-weight:500;border-top:1px dashed var(--blue-soft)}
.vision-menu li.on{background:var(--blue);color:var(--white)}
.vision-copy{left:638px;top:140px;width:350px;color:var(--white)}
.vision-copy h2{font-size:34px;font-weight:500}
.vision-copy p{margin-top:32px;font-size:15px;line-height:1.6}
.read-more{display:flex;align-items:center;gap:8px;font-size:13px;font-weight:500}
.vision-copy .read-more{margin-top:24px}

/* why */
.why-title{left:0;top:1580px;width:1200px}
.why-card{top:1665px;width:280px}
.why-frame{height:231px;border:2px dashed var(--blue-soft);padding:9px;border-radius:3px}
.why-frame div{width:100%;height:100%;border-radius:6px}
.why-card h3{margin-top:38px;font-size:19px;font-weight:500;line-height:1.45}
.why-card p{margin-top:16px;font-size:13px;line-height:1.4}

/* working */
.working{left:0;top:2121px;width:1200px;height:620px;background:var(--blue);color:var(--white)}
.working .eyebrow{left:0;top:24px;width:1200px;text-align:center;font-size:19px;font-weight:500}
.working h2{left:0;top:52px;width:1200px;text-align:center;font-size:33px;font-weight:700}
.working-art{left:95px;top:172px;width:393px;height:365px;background:linear-gradient(160deg,#f5f7fc,#dfe6f6);border-radius:4px}
.approach{left:526px;top:124px;width:580px}
.approach h3{font-size:20px;font-weight:600}
.approach p{margin-top:12px;font-size:13px;line-height:1.35}
.ticks{margin-top:24px;list-style:none}
.ticks li{display:flex;align-items:center;gap:18px;font-size:13px;height:41px}
.join{left:526px;top:450px;width:580px}
.join h3{font-size:20px;font-weight:600}
.join p{margin-top:20px;font-size:13px;line-height:1.7}
.join-form{margin-top:18px;display:flex;gap:25px}
.join-form .field{width:279px;height:32px;background:var(--white);color:#777;font-size:13px;padding:7px 14px;border-radius:2px}
.join-form .go{width:112px;height:32px;background:var(--blue-soft);font-size:13px;font-weight:500;display:flex;align-items:center;justify-content:center;border-radius:2px}

/* testimonials */
.praise{left:0;top:2741px;width:1200px;height:494px;background:var(--blue-mist)}
.eyebrow-blue{color:var(--blue);font-size:17px;font-weight:500;text-align:center;width:1200px;left:0}
.title-blue{color:var(--blue);font-size:30px;font-weight:500;text-align:center;width:1200px;left:0}
.quote{top:172px;width:281px;height:265px;background:var(--white);border-radius:6px;box-shadow:0 2px 8px rgba(0,0,0,.06);padding:64px 22px 0 21px;color:#777}
.quote.lead{background:var(--blue);color:var(--white)}
.quote p{font-size:14px;line-height:1.65;height:130px}
.quote .who{display:flex;align-items:center;gap:22px;margin-top:6px}
.avatar{width:60px;height:60px;border-radius:50%;background:linear-gradient(135deg,#f3c04b,#e79a2b);flex:none}
.avatar.grey{background:linear-gradient(135deg,#d9d4cf,#b8b1aa)}
.who b{display:block;font-size:13px;font-weight:600;color:var(--ink)}
.who small{display:block;font-size:11px;color:#666}
.quote.lead .who b,.quote.lead .who small{color:var(--white)}
.stars{font-size:18px;letter-spacing:4px;color:var(--blue-mid)}
.stars i{font-style:normal;color:#d0d0d0}
.quote.lead .stars{color:var(--white)}
.dots{left:566px;top:468px;display:flex;gap:6px}
.dots span{width:10px;height:10px;border-radius:50%;background:#cfd6e2}
.dots span.on{background:var(--blue-mid)}

/* blog */
.post{top:3365px;width:317px;height:459px;border:1.5px solid var(--blue-mid);border-radius:4px;padding:15px 15px 0}
.post.shaded{background:var(--blue-mist);border-color:var(--blue-mist)}
.post-img{height:230px;border-radius:3px}
.meta{display:flex;align-items:center;gap:14px;margin-top:22px;padding-left:4px}
.meta .avatar{width:34px;height:34px;background:var(--blue-pale)}
.meta b{display:block;font-size:18px;font-weight:500;line-height:1}
.meta small{font-size:12px;color:#888;word-spacing:2px}
.post h3{margin-top:22px;font-size:19px;font-weight:500;line-height:1.45;padding-left:4px}
.post-foot{display:flex;justify-content:space-between;align-items:center;margin-top:22px;font-size:12px;color:#888}
.post-foot .read-more{color:var(--blue-mid);font-size:13px}

/* footer */
.footer{left:0;top:3888px;width:1200px;height:348px;background:var(--footer);color:#dfe4ec}
.footer .brand{position:absolute;left:90px;top:60px;color:var(--white)}
.contact-line{display:flex;gap:14px;font-size:12px;line-height:1.55}
.footer h4{font-size:12px;font-weight:600;color:var(--blue-soft)}
.footer ul{list-style:none;margin-top:18px}
.footer li{font-size:12px;height:33px}
.news-label{font-size:12px;margin-top:18px}
.news-field{margin-top:10px;width:247px;height:46px;background:var(--blue-mist);color:#777;font-size:12px;padding:14px 12px}
.news-send{margin-top:22px;width:107px;height:43px;background:var(--blue-mid);color:var(--white);font-size:12px;font-weight:600;display:flex;align-items:center;justify-content:center;border-radius:3px}
.copyright{font-size:12px;margin-top:30px}
</style>
</head>
<body>

<header class="abs topbar">
  <div class="brand"><span class="brand-mark"></span><div><div class="brand-name">Halvorn</div><div class="brand-sub">Ventures International</div></div></div>
  <a class="nav-link active" style="left:436px">Home</a>
  <a class="nav-link" style="left:531px">About us</a>
  <a class="nav-link" style="left:650px">Services</a>
  <a class="nav-link" style="left:769px">Contact us</a>
  <div class="abs consult">
    <span class="consult-icon"><svg width="22" height="22" viewBox="0 0 24 24"><path fill="#34398a" d="M6.6 10.8a15.1 15.1 0 0 0 6.6 6.6l2.2-2.2c.3-.3.7-.4 1-.2 1.1.4 2.3.6 3.6.6.6 0 1 .4 1 1V20c0 .6-.4 1-1 1A17 17 0 0 1 3 4c0-.6.4-1 1-1h3.5c.6 0 1 .4 1 1 0 1.3.2 2.5.6 3.6.1.3 0 .7-.2 1z"/></svg></span>
    <div><small>Request</small><b>CONSULT CALL</b></div>
  </div>
</header>

<section class="abs hero">
  <div class="abs hero-disc"></div>
  <div class="abs hero-portrait" role="img" aria-label="Portrait of the consultant in a blue suit"></div>
  <h1 class="abs">Creating Safer Work Environments Through Strong Leadership</h1>
  <p class="abs">If you are not willing to risk the usual, you will have to settle for the ordinary. I’m here to help and share my story.</p>
  <div class="abs signature" role="img" aria-label="Handwritten signature of Martin Halvorn"></div>
  <a class="abs btn-primary">GET FREE SESSION</a>
</section>

<h2 class="abs h-section possible-title">HOW IT’S POSSIBLE</h2>
<p class="abs possible-lead">We believe that effective leadership is the cornerstone of a safe and productive workplace. Our comprehensive approach includes:</p>

<div class="abs pillar" style="left:78px">
  <div class="pillar-ring"><span><svg width="120" height="90" viewBox="0 0 120 90"><g fill="#4a5563"><circle cx="16" cy="30" r="7"/><rect x="8" y="39" width="16" height="30" rx="4"/><circle cx="34" cy="26" r="7"/><rect x="26" y="35" width="16" height="34" rx="4"/><circle cx="86" cy="26" r="7"/><rect x="78" y="35" width="16" height="34" rx="4"/><circle cx="104" cy="30" r="7"/><rect x="96" y="39" width="16" height="30" rx="4"/></g><g fill="#0677BA"><circle cx="60" cy="16" r="9"/><rect x="48" y="28" width="24" height="56" rx="5"/></g></svg></span></div>
  <h3>Leadership Training</h3>
  <p>Equipping leaders with the skills and knowledge to drive safety initiatives and inspire their teams</p>
</div>
<div class="abs pillar" style="left:442px">
  <div class="pillar-ring"><span><svg width="100" height="100" viewBox="0 0 100 100" fill="none" stroke="#1c1c1c" stroke-width="4"><circle cx="50" cy="50" r="26"/><circle cx="50" cy="50" r="13" fill="#0677BA" stroke="none"/><circle cx="50" cy="50" r="6" fill="#fff" stroke="none"/><path d="M18 40a34 34 0 0 1 50-22M82 60a34 34 0 0 1-50 22"/><path d="M62 12l8 6-8 6M38 88l-8-6 8-6"/></svg></span></div>
  <h3>Process Development</h3>
  <p>Assisting organizations in creating and implementing processes that prioritize safety at every level.</p>
</div>
<div class="abs pillar" style="left:804px">
  <div class="pillar-ring"><span><svg width="90" height="90" viewBox="0 0 90 90"><g fill="#0054AA"><path d="M45 6l3 7 7 1-5 5 1 7-6-3-6 3 1-7-5-5 7-1z"/><path d="M18 22l2 5 5 1-4 3 1 5-4-3-5 3 1-5-4-3 5-1z"/><path d="M72 22l2 5 5 1-4 3 1 5-4-3-5 3 1-5-4-3 5-1z"/></g><g fill="none" stroke="#1c1c1c" stroke-width="4" stroke-linejoin="round"><path d="M22 48l23-10 23 10-23 10z"/><path d="M22 48v22l23 12 23-12V48"/><path d="M45 58v24"/></g></svg></span></div>
  <h3>Performance Assessment</h3>
  <p>Evaluating the impact of leadership on safety performance and identifying areas for improvement.</p>
</div>

<section class="abs vision">
  <div class="abs vision-photo" role="img" aria-label="The consultant speaking on stage at a leadership event"></div>
  <svg class="abs" style="left:0;top:0" width="1034" height="449" viewBox="0 0 1034 449"><path fill="#0054AA" d="M690 0H1034V449H540C540 250 560 70 690 0z"/></svg>
  <div class="abs vision-menu">
    <div class="xp"><b>12+</b><span>YEARS<br>EXPERIENCE</span></div>
    <ul>
      <li>Story <svg width="36" height="12" viewBox="0 0 36 12"><path d="M0 6h34M28 1l6 5-6 5" fill="none" stroke="currentColor" stroke-width="1.6"/></svg></li>
      <li class="on">Vision <svg width="36" height="12" viewBox="0 0 36 12"><path d="M0 6h34M28 1l6 5-6 5" fill="none" stroke="currentColor" stroke-width="1.6"/></svg></li>
      <li>Leadership <svg width="36" height="12" viewBox="0 0 36 12"><path d="M0 6h34M28 1l6 5-6 5" fill="none" stroke="currentColor" stroke-width="1.6"/></svg></li>
      <li>Awards <svg width="36" height="12" viewBox="0 0 36 12"><path d="M0 6h34M28 1l6 5-6 5" fill="none" stroke="currentColor" stroke-width="1.6"/></svg></li>
      <li>Our Partners <svg width="36" height="12" viewBox="0 0 36 12"><path d="M0 6h34M28 1l6 5-6 5" fill="none" stroke="currentColor" stroke-width="1.6"/></svg></li>
    </ul>
  </div>
  <div class="abs vision-copy">
    <h2>Vision</h2>
    <p>My focus is on helping organizations to understand the impact that leaders have on safety performance and how they build the processes to make that happen</p>
    <a class="read-more">Read more <svg width="26" height="10" viewBox="0 0 26 10"><path d="M0 5h24M19 1l5 4-5 4" fill="none" stroke="currentColor" stroke-width="1.5"/></svg></a>
  </div>
</section>

<h2 class="abs h-section why-title">WHY CHOOSE US?</h2>
<div class="abs why-card" style="left:108px">
  <div class="why-frame"><div role="img" aria-label="Close-up of hands adjusting a necktie" style="background:linear-gradient(135deg,#2d3340,#6d7f9c 60%,#c9cdd6)"></div></div>
  <h3>Expert Leadership Training</h3>
  <p>We provide comprehensive training programs designed to equip leaders with the skills and knowledge necessary to drive safety initiatives and inspire their teams.</p>
</div>
<div class="abs why-card" style="left:460px">
  <div class="why-frame"><div role="img" aria-label="Smiling professional working at a laptop" style="background:linear-gradient(135deg,#4a3b30,#9a7f68 55%,#d9cbbd)"></div></div>
  <h3>Innovative Process Development</h3>
  <p>Our team assists organizations in creating and implementing safety processes that are both effective and sustainable.</p>
</div>
<div class="abs why-card" style="left:810px">
  <div class="why-frame"><div role="img" aria-label="Two executives reviewing documents at a desk" style="background:linear-gradient(135deg,#e8ebef,#8d96a3 50%,#2f3440)"></div></div>
  <h3>Comprehensive Performance Assessment</h3>
  <p>We evaluate the impact of leadership on safety performance, identifying strengths and areas for improvement to help organizations achieve their safety goals.</p>
</div>

<section class="abs working">
  <div class="abs eyebrow">We Know The Way To Success</div>
  <h2 class="abs">WORKING WITH US</h2>
  <div class="abs working-art" role="img" aria-label="Illustration of team members climbing stairs toward a leader with an idea"></div>
  <div class="abs approach">
    <h3>Our Approach</h3>
    <p>We believe that every organization is unique, and so are its challenges and opportunities. Our tailored approach ensures that our solutions are customized to meet your specific needs, helping you create a safer and more productive workplace</p>
    <ul class="ticks">
      <li><svg width="20" height="20" viewBox="0 0 20 20" fill="none" stroke="#fff" stroke-width="1.5"><path d="M17 9a7 7 0 1 1-3-5.6"/><path d="M6 9.5l3 3 9-9"/></svg>Cost-Effective Services</li>
      <li><svg width="20" height="20" viewBox="0 0 20 20" fill="none" stroke="#fff" stroke-width="1.5"><path d="M17 9a7 7 0 1 1-3-5.6"/><path d="M6 9.5l3 3 9-9"/></svg>Helps Reduce Business Risks</li>
      <li><svg width="20" height="20" viewBox="0 0 20 20" fill="none" stroke="#fff" stroke-width="1.5"><path d="M17 9a7 7 0 1 1-3-5.6"/><path d="M6 9.5l3 3 9-9"/></svg>Management of Employee Performance</li>
      <li><svg width="20" height="20" viewBox="0 0 20 20" fill="none" stroke="#fff" stroke-width="1.5"><path d="M17 9a7 7 0 1 1-3-5.6"/><path d="M6 9.5l3 3 9-9"/></svg>Increasing Company’s Agility</li>
    </ul>
  </div>
  <div class="abs join">
    <h3>Join Us</h3>
    <p>Take the first step towards a safer workplace. Explore our services, learn about our approach, and see how we can help your organization achieve its safety objectives.</p>
    <div class="join-form"><div class="field">Enter your email</div><div class="go">Join Now</div></div>
  </div>
</section>

<section class="abs praise">
  <div class="abs eyebrow-blue" style="top:46px">TESTIMONIALS</div>
  <h2 class="abs title-blue" style="top:70px">What do people praise about HVI?</h2>
  <div class="abs quote lead" style="left:112px">
    <p>They are a great partner to work with. Will listen to what your needs are and will provide amazing solutions.</p>
    <div class="who"><span class="avatar" role="img" aria-label="Client portrait"></span><div><b>Corin Vale</b><small>Veltmoor Power</small><div class="stars">★★★★★</div></div></div>
  </div>
  <div class="abs quote" style="left:462px">
    <p>They are a great partner to work with. Will listen to what your needs are and will provide amazing solutions.</p>
    <div class="who"><span class="avatar" role="img" aria-label="Client portrait"></span><div><b>Corin Vale</b><small>Veltmoor Power</small><div class="stars">★★★<i>★★</i></div></div></div>
  </div>
  <div class="abs quote" style="left:812px">
    <p>Dana and Kestrel Works did an excellent job under very tight (some might say unreasonable) deadlines.</p>
    <div class="who"><span class="avatar grey" role="img" aria-label="Client portrait"></span><div><b>Tobin Marsh</b><small>Larkspire Communications</small><div class="stars">★★★<i>★★</i></div></div></div>
  </div>
  <div class="abs dots"><span class="on"></span><span></span><span></span><span></span></div>
</section>

<div class="abs eyebrow-blue" style="top:3268px">NEWS &amp; UPDATES</div>
<h2 class="abs title-blue" style="top:3296px;font-size:33px;font-weight:600;color:var(--blue-mid)">Latest from our Blog Post</h2>

<article class="abs post shaded" style="left:102px">
  <div class="post-img" role="img" aria-label="Handshake over a desk with documents" style="background:linear-gradient(135deg,#3c4a3e,#8f9a8f 55%,#e3e6e3)"></div>
  <div class="meta"><span class="avatar"></span><div><b>Admin</b><small>April 20, 2024 &nbsp; 0 Comments</small></div></div>
  <h3>Unlocking Success: Top Eight Tips for Leadership Recruitment.</h3>
  <div class="post-foot"><span>3 MONTHS AGO</span><a class="read-more">Read more <svg width="26" height="10" viewBox="0 0 26 10"><path d="M0 5h24M19 1l5 4-5 4" fill="none" stroke="currentColor" stroke-width="1.5"/></svg></a></div>
</article>
<article class="abs post" style="left:441px">
  <div class="post-img" role="img" aria-label="Site workers in hard hats and safety vests at a meeting" style="background:linear-gradient(135deg,#d9c9a8,#e07a2c 50%,#4b4a47)"></div>
  <div class="meta"><span class="avatar"></span><div><b>Admin</b><small>April 20, 2024 &nbsp; 0 Comments</small></div></div>
  <h3>Unlocking Success: Top Eight Tips for Leadership Recruitment.</h3>
  <div class="post-foot"><span>3 MONTHS AGO</span><a class="read-more">Read more <svg width="26" height="10" viewBox="0 0 26 10"><path d="M0 5h24M19 1l5 4-5 4" fill="none" stroke="currentColor" stroke-width="1.5"/></svg></a></div>
</article>
<article class="abs post" style="left:783px">
  <div class="post-img" role="img" aria-label="Two colleagues talking at a bright table" style="background:linear-gradient(135deg,#f1ece6,#c99f8e 55%,#6f5246)"></div>
  <div class="meta"><span class="avatar"></span><div><b>Admin</b><small>April 20, 2024 &nbsp; 0 Comments</small></div></div>
  <h3>Unlocking Success: Top Eight Tips for Leadership Recruitment.</h3>
  <div class="post-foot"><span>3 MONTHS AGO</span><a class="read-more">Read more <svg width="26" height="10" viewBox="0 0 26 10"><path d="M0 5h24M19 1l5 4-5 4" fill="none" stroke="currentColor" stroke-width="1.5"/></svg></a></div>
</article>

<footer class="abs footer">
  <div class="brand"><span class="brand-mark"></span><div><div class="brand-name" style="font-size:30px">Halvorn</div><div class="brand-sub">Ventures International</div></div></div>
  <div class="abs" style="left:88px;top:128px;width:250px">
    <div class="contact-line"><svg width="14" height="16" viewBox="0 0 14 16"><path d="M7 15s5-5 5-9A5 5 0 0 0 2 6c0 4 5 9 5 9z" fill="none" stroke="#7BADD7" stroke-width="1.4"/><circle cx="7" cy="6" r="1.8" fill="#7BADD7"/></svg><span>4120 Alder Lane, Riverton,<br>British Columbia, Canada.<br>V0X 2B3</span></div>
    <div class="contact-line" style="margin-top:14px"><svg width="16" height="14" viewBox="0 0 16 14"><rect x="1" y="2" width="14" height="10" rx="1" fill="none" stroke="#7BADD7" stroke-width="1.4"/><path d="M1 3l7 5 7-5" fill="none" stroke="#7BADD7" stroke-width="1.4"/></svg><span>martin@halvorn.example</span></div>
    <div class="contact-line" style="margin-top:22px"><svg width="16" height="16" viewBox="0 0 24 24"><path fill="#7BADD7" d="M6.6 10.8a15.1 15.1 0 0 0 6.6 6.6l2.2-2.2c.3-.3.7-.4 1-.2 1.1.4 2.3.6 3.6.6.6 0 1 .4 1 1V20c0 .6-.4 1-1 1A17 17 0 0 1 3 4c0-.6.4-1 1-1h3.5c.6 0 1 .4 1 1 0 1.3.2 2.5.6 3.6.1.3 0 .7-.2 1z"/></svg><span>1-555-014-2288</span></div>
  </div>
  <div class="abs" style="left:478px;top:76px">
    <h4>Company</h4>
    <ul><li>Home</li><li>Services</li><li>About us</li><li>Blog</li><li>Contact Us</li></ul>
  </div>
  <div class="abs" style="left:694px;top:76px">
    <h4>Our Social Media</h4>
    <ul><li>Portfolio</li><li>Gallery</li><li>Journal</li><li>Photos</li><li>Community</li><li>Updates</li></ul>
  </div>
  <div class="abs" style="left:866px;top:76px">
    <h4>Join a Newsletter</h4>
    <div class="news-label">Your Email</div>
    <div class="news-field">Enter Your Email</div>
    <div class="news-send">Send</div>
    <div class="copyright">Copyright Halvorn International</div>
  </div>
</footer>

</body>
</html>
```